IT Networking company requires a Brochure Design

We require a new design for our company brochure. We'd like a single double-sided A4 design where the front page will have company related information and services and the rear to have customer testimonials. Please refer to attached document for info as well as our website www.tevralink.com.au. maintain website colour schema as we are an environmentally friendly organisation

Industry/Entity Type

It Company

```html
<!DOCTYPE html>
<html lang="en">
<head>
<meta charset="utf-8">
<title>Tevralink Brochure</title>
<link rel="stylesheet" href="https://fonts.googleapis.com/css2?family=Poppins:wght@500;600;700&display=swap">
<style>
  :root {
    --olive: #4a5a2b;
    --olive-text: #55672f;
    --ink: #3a3a3a;
    --paper: #ffffff;
  }
  * { margin: 0; padding: 0; box-sizing: border-box; }
  html, body { width: 1200px; height: 845px; overflow: hidden; background: var(--paper); }
  .brochure {
    position: relative; width: 1200px; height: 845px; overflow: hidden;
    font-family: "Poppins", Arial, sans-serif; color: var(--ink);
    background: var(--paper);
  }
  .band { position: absolute; left: 0; width: 100%; background: var(--olive); }
  .band--top { top: 0; height: 30px; }
  .band--bottom { bottom: 0; height: 33px; }
  .hero-photo {
    position: absolute; left: 0; top: 30px; width: 596px; height: 260px;
    background: linear-gradient(115deg, #d9d9d9 0%, #eeeeee 45%, #ffffff 85%);
  }
  .shapes { position: absolute; left: 0; top: 0; }
  .headline {
    position: absolute; left: 27px; top: 331px;
    color: var(--paper); font-weight: 600; font-size: 22px; line-height: 34px;
    text-transform: uppercase; letter-spacing: 0.1px; white-space: nowrap;
  }
  .intro {
    position: absolute; left: 27px; top: 556px; width: 450px;
    font-size: 9.8px; font-weight: 600; line-height: 17.4px; text-transform: uppercase;
    color: var(--ink);
  }
  .intro p { margin-bottom: 17.4px; }
  .column { position: absolute; left: 620px; width: 560px; }
  .column--services { top: 52px; }
  .column--benefits { top: 340px; }
  .section-title {
    color: var(--olive-text); font-weight: 700; font-size: 21px; line-height: 26px;
    text-transform: uppercase; margin-bottom: 8px;
  }
  .lead { font-size: 10.8px; font-weight: 600; line-height: 17.3px; padding-left: 10px; text-transform: uppercase; }
  .list { list-style: none; }
  .list li {
    position: relative; padding-left: 11px;
    font-size: 10.8px; font-weight: 600; line-height: 17.3px; text-transform: uppercase;
  }
  .list li::before {
    content: ""; position: absolute; left: 0; top: 7px; width: 5px; height: 5px;
    border-radius: 50%; background: var(--olive-text);
  }
</style>
</head>
<body>
<main class="brochure">
  <div class="band band--top"></div>
  <div class="hero-photo" role="img" aria-label="Black and white photo of hands typing on a laptop with a faint globe"></div>

  <svg class="shapes" width="1200" height="845" viewBox="0 0 1200 845" aria-hidden="true">
    <defs>
      <linearGradient id="mistFade" x1="0" y1="0" x2="1" y2="1">
        <stop offset="0" stop-color="#e9e9e9"/>
        <stop offset="1" stop-color="#d8d8d8"/>
      </linearGradient>
    </defs>
    <polygon points="0,534 526,534 452,812 0,812" fill="url(#mistFade)"/>
    <polygon points="0,289 562,289 600,411 562,534 0,534" fill="var(--olive)"/>
  </svg>

  <h1 class="headline">Tevralink is a privately owned company<br>that provides market leading<br>technology solutions across a wide<br>range of industries throughout<br>Australia and Asia Pacific.</h1>

  <section class="intro">
    <p>Based in beautiful Sydney, our business, structure and technology solutions are all designed to help customers meet their business objectives. We design, deploy and manage technology solutions through our specialist businesses which are product solutions, integrated solutions and managed services.</p>
    <p>Our strategic consulting team based on a wealth of technical and business knowledge, enables our customers to align their ICT programs with one or more business objectives to ensure that their ICT investment is clearly defined in terms of business outcomes.</p>
    <p>"Connected by nature"</p>
  </section>

  <section class="column column--services">
    <h2 class="section-title">Services</h2>
    <ul class="list">
      <li>Networking – Integration</li>
      <li>Cloud Computing</li>
      <li>Security</li>
      <li>Business Continuity / Disaster Recovery</li>
      <li>WAN Acceleration</li>
      <li>Virtualisation (Brellum, Quorvane Host, Lumetra Core)</li>
      <li>Enterprise Thin Clients</li>
      <li>Nordhal Solutions</li>
      <li>Sandivo Solutions</li>
      <li>Palowen Solutions</li>
      <li>End-User Computing</li>
      <li>Support</li>
    </ul>
  </section>

  <section class="column column--benefits">
    <h2 class="section-title">Benifits</h2>
    <p class="lead">With Tevralink, your organisation will be able to:</p>
    <ul class="list">
      <li>Enable business driven ICT transformation</li>
      <li>Optimise return on ICT investments</li>
      <li>Manage ICT related risks</li>
      <li>Reduce costs</li>
      <li>Increase productivity</li>
      <li>Secure your data and systems</li>
      <li>Ensure efficient procurement and timely supply of ICT hardware</li>
      <li>Manage procurement contracts for hardware from multiple vendors</li>
      <li>Ensure efficient deployment of equipment</li>
      <li>Devise accurate plans and budgets for hardware and software upgrades</li>
      <li>Ensure licensing compliance</li>
      <li>Maintain standardised environments to minimise support overheads</li>
      <li>Integrate the latest technology -virtualised infrastructure – lowering costs, improving agility and increasing flexibility</li>
      <li>Optimise ICT service delivery and agility</li>
      <li>Optimise ICT procurement</li>
      <li>Shorten ICT project lead times</li>
      <li>Respond quickly to changing capacity requirements</li>
      <li>Align expenditure with consumption</li>
    </ul>
  </section>

  <div class="band band--bottom"></div>
</main>
</body>
</html>
```